Postcard Design

I am a practicing Obstetrician and Gynecologist. I am working at a clinic called Corvane Ridge Health System. I am looking for a design of a personal advertisement card that can be mailed, handed out, or sent an an electronic copy to the local newspaper to be placed as an ad. I previously worked for another clinic called TBW. They had an ad on my I liked very much, but I cannot use it. It is proprietary to them. I would like something like it. Copy attached. I want my foto and text. I have Printhollow Business Cards with Corvane Ridge and Stationary already. Access permitted. I would like to stay within that light blue - light green color scheme. I want the card to have me come across as competent and knowledgeable, but also as gentle, compassionate, benevolent, caring, knowledgeable, competent. Obviously, it has to appeal to women.

Target Market(s)

Public, patients, women

Industry/Entity Type

Electronic

Requirements
Nice to have
• A sophisticated, tasteful and inspiring maternity care image is very hard to find. I love the one on my business card. If it or something like it could be found and incorporated, that would be nice. I like a warm, soft, friendly font, Calibri light italic, Archer, Gotham. Describes nicely:Archer, the colorful slab serif. Sweet but not saccharine, earnest but not grave, Archer is designed to hit just the right notes of forthrightness, credibility, and charm.

```html
<!DOCTYPE html>
<html lang="en">
<head>
<meta charset="utf-8">
<title>Anselm R Tovermark, MD — Corvane Ridge Health System</title>
<link rel="stylesheet" href="https://fonts.googleapis.com/css2?family=Lato:wght@400&display=swap">
<style>
  :root {
    --card-white: #fbfdff;
    --net-blue: #cfe0f3;
    --net-blue-soft: #eaf2fa;
    --mint-soft: #e6f4ee;
    --band-top: #c4d8ef;
    --band-bottom: #dbeaf1;
    --band-rule: #9fbbdc;
    --ink: #2f3439;
    --edge: #9aa3ab;
    --portrait-light: #f3ece2;
    --portrait-warm: #cbb49c;
    --family-light: #f1d2b6;
    --family-deep: #7a4a33;
  }
  html, body {
    margin: 0;
    padding: 0;
    width: 1200px;
    height: 702px;
    overflow: hidden;
    background: #ffffff;
  }
  .card {
    position: relative;
    width: 1200px;
    height: 702px;
    box-sizing: border-box;
    border: 2px solid var(--edge);
    background: var(--card-white);
    font-family: "Lato", "Helvetica Neue", Arial, sans-serif;
    color: var(--ink);
    overflow: hidden;
  }
  .card__backdrop {
    position: absolute;
    inset: 0;
    background:
      radial-gradient(ellipse 70% 45% at 20% 12%, var(--net-blue) 0%, transparent 70%),
      radial-gradient(ellipse 60% 40% at 30% 98%, var(--net-blue) 0%, transparent 70%),
      radial-gradient(ellipse 45% 45% at 96% 92%, var(--mint-soft) 0%, transparent 70%),
      linear-gradient(180deg, var(--net-blue-soft), var(--card-white) 45%, var(--net-blue-soft));
  }
  .system-name {
    position: absolute;
    right: 60px;
    top: 64px;
    margin: 0;
    font-size: 30px;
    font-weight: 400;
    line-height: 1;
  }
  .identity-band {
    position: absolute;
    left: 0;
    right: 0;
    top: 127px;
    height: 151px;
    background: linear-gradient(180deg, var(--band-top) 0%, var(--band-top) 54%, var(--band-bottom) 54%, var(--band-bottom) 100%);
    border-top: 1px solid var(--band-rule);
    border-bottom: 1px solid var(--band-rule);
    box-sizing: border-box;
  }
  .identity-band__rule {
    position: absolute;
    left: 0;
    right: 0;
    top: 80px;
    height: 2px;
    background: var(--band-rule);
  }
  .doctor-name {
    position: absolute;
    left: 66px;
    top: 14px;
    margin: 0;
    font-size: 50px;
    font-weight: 400;
    line-height: 1.1;
  }
  .credential {
    position: absolute;
    left: 68px;
    top: 96px;
    margin: 0;
    font-size: 36px;
    font-weight: 400;
    line-height: 1.1;
  }
  .photo {
    position: absolute;
    top: 283px;
    height: 287px;
  }
  .photo--portrait {
    left: 457px;
    width: 195px;
    background: linear-gradient(160deg, var(--portrait-light) 0%, #e6d9c9 50%, var(--portrait-warm) 100%);
  }
  .photo--family {
    left: 665px;
    width: 500px;
    background: linear-gradient(110deg, var(--family-deep) 0%, #b98463 30%, var(--family-light) 60%, #e8b996 80%, var(--family-deep) 100%);
  }
  .contact {
    position: absolute;
    left: 68px;
    top: 440px;
    margin: 0;
    font-style: normal;
    font-size: 33px;
    font-weight: 400;
    line-height: 48px;
  }
  .contact__line { display: block; }
  .contact__line--gap { margin-top: 10px; }
</style>
</head>
<body>
  <main class="card">
    <div class="card__backdrop" role="img" aria-label="Soft light blue woven net pattern across a white background"></div>

    <p class="system-name">Corvane Ridge Health System</p>

    <header class="identity-band">
      <div class="identity-band__rule"></div>
      <h1 class="doctor-name">Anselm R Tovermark, MD</h1>
      <p class="credential">Board Certified</p>
    </header>

    <div class="photo photo--portrait" role="img" aria-label="Portrait photograph of the physician, a smiling older man in a white shirt"></div>
    <div class="photo photo--family" role="img" aria-label="Photograph of a mother lovingly lifting her baby"></div>

    <address class="contact">
      <span class="contact__line">214-B Calle Marisol</span>
      <span class="contact__line">Sumay Bay, Guam, 96920</span>
      <span class="contact__line contact__line--gap">Phone 671.555.0142</span>
      <span class="contact__line">Fax 671.555.0187</span>
    </address>
  </main>
</body>
</html>
```